HUSH: Hush Until Stories Happen school library event

I need two poster designs for Hush Until Stories Happen (HUSH) in BC, requested by the PCSMG--Pacific Coast School Media Guild. One should be for elementary students and one for high school. I want the date (Monday, October 26, 2020) and Hush Until Stories Happen. I would like the posters in English and in French. French is : Ferme Ton Écran Maintenant! I'm including last year's posters as examples. I would like to be able to print the poster files on 11x17 paper.

• -The phrase "Hush Until Stories Happen" for the English version; "Ferme Ton Écran Maintenant" for the French version.
-Include the organization name: Pacific Coast School Media Guild
-The date: Monday, October 26, 2020
• I would like the elementary version to be bright and colourful--fun for younger kids. I would like the high school version to be a bit more mature for the older students. Can still be bright and colourful.

```html
<!DOCTYPE html>
<html lang="fr">
<head>
<meta charset="utf-8">
<title>Ferme Ton Écran Maintenant — Pacific Coast School Media Guild</title>
<link rel="stylesheet" href="https://fonts.googleapis.com/css2?family=Poppins:wght@300;400;800&family=Gochi+Hand&display=swap">
<style>
  :root {
    --sky: #1f9ad4;
    --plum: #2e1a47;
    --magenta: #b3328f;
    --sun: #f5da0b;
    --sun-soft: #f8e65a;
    --paper: #ffffff;
    --page-bg: #ffffff;
  }
  html, body {
    margin: 0;
    padding: 0;
    width: 1199px;
    height: 1200px;
    overflow: hidden;
    background: var(--page-bg);
  }
  .canvas {
    width: 1199px;
    height: 1200px;
    display: flex;
    align-items: center;
    justify-content: center;
  }
  .poster {
    width: 738px;
    height: 1140px;
    display: block;
  }
  .poster-bg { fill: var(--sky); }
  .sun-circle { fill: var(--magenta); }
  .illustration-area { fill: url(#illustration-tone); }
  .tone-start { stop-color: var(--sun); }
  .tone-end { stop-color: var(--sun-soft); }
  .big-letter {
    font-family: "Poppins", sans-serif;
    font-weight: 800;
  }
  .big-letter--dark { fill: var(--plum); }
  .big-letter--light { fill: var(--paper); }
  .phrase-word {
    font-family: "Gochi Hand", cursive;
    font-size: 52px;
  }
  .phrase-word--light { fill: var(--paper); }
  .phrase-word--dark { fill: var(--plum); }
  .org-name {
    font-family: "Poppins", sans-serif;
    font-weight: 300;
    font-size: 21px;
    letter-spacing: 1px;
    fill: var(--paper);
  }
  .event-date {
    font-family: "Poppins", sans-serif;
    fill: var(--plum);
  }
  .event-date__day { font-weight: 800; font-size: 38px; }
  .event-date__line { font-weight: 400; font-size: 40px; }
</style>
</head>
<body>
<main class="canvas">
  <svg class="poster" viewBox="0 0 825 1275" xmlns="http://www.w3.org/2000/svg">
    <defs>
      <linearGradient id="illustration-tone" x1="0" y1="0" x2="0" y2="1">
        <stop class="tone-start" offset="0"/>
        <stop class="tone-end" offset="1"/>
      </linearGradient>
    </defs>

    <rect class="poster-bg" width="825" height="1275"/>

    <circle class="sun-circle" cx="545" cy="263" r="215"/>

    <rect class="illustration-area" x="150" y="220" width="470" height="800"
      role="img"
      aria-label="Illustration area: a hand in a striped sleeve holding up an open book"/>

    <text class="big-letter big-letter--dark" x="60" y="296" font-size="320">F</text>
    <text class="big-letter big-letter--light" x="318" y="435" font-size="320">T</text>
    <text class="big-letter big-letter--light" x="530" y="611" font-size="300">É</text>

    <text class="phrase-word phrase-word--light" x="63" y="178">ferme</text>
    <text class="phrase-word phrase-word--dark" x="262" y="388">ton</text>
    <text class="phrase-word phrase-word--dark" x="395" y="523">écran</text>
    <text class="phrase-word phrase-word--dark" x="470" y="690">maintenant</text>

    <g class="org-name" transform="rotate(-12 690 860)">
      <text x="705" y="830" text-anchor="middle">Pacific Coast</text>
      <text x="700" y="866" text-anchor="middle">School Media</text>
      <text x="725" y="902" text-anchor="middle">Guild</text>
    </g>

    <g class="event-date">
      <text class="event-date__day" x="103" y="1100" transform="rotate(-4 103 1100)">Lundi</text>
      <text class="event-date__line" x="72" y="1148" transform="rotate(5 72 1148)">26 Octobre</text>
      <text class="event-date__line" x="103" y="1200">2020</text>
    </g>
  </svg>
</main>
</body>
</html>
```